Retro game shop business card design

We need a card designed both front and back. we already have a logo. The business name is called Brisk Copper Atlas and we work on customizing and modifying old velmora zuma tabs. Our website is briskcopperatlas.com

our business cards are often shown in glintly posts ans should be designed so that you can easy identify and see in am image. @briskcopperatlas.

Target Market(s)

men 13-40

Contact Information for Business Card

should have logo, wesbite, and if possible some artwork related to zuma tab mods

Font styles to use
Sans Serif

Colors

Designer to choose colors to be used in the design.

Requirements
Must have
• logo, website url www.briskcopperatlas.com, hastag #zumatabmods, email, support@briskcopperatlas.com. zuma tab imagry only (illustration preffered)
Nice to have
• illustrations, graphic design with zuma tab mods (see glintly #zumatabmods)
Should not have
• childlike depictions of zumatabs, kids, anything unrelated to zuma tab mods, no hands, no bertil, no pixel art

```html
<!DOCTYPE html>
<html lang="en">
<head>
<meta charset="utf-8">
<title>Brisk Copper Atlas – Business Card</title>
<link rel="stylesheet" href="https://fonts.googleapis.com/css2?family=Open+Sans:wght@400;600;800&display=swap">
<style>
  :root {
    --backdrop: #3e424c;
    --card-white: #ffffff;
    --card-black: #1d1a1b;
    --ink-dark: #1a1a1a;
    --ink-grey: #8a8a8a;
    --ink-light: #f2f2f2;
    --rule-dark: #2a2a2a;
    --rule-light: #bdbdbd;
  }
  * { box-sizing: border-box; margin: 0; padding: 0; }
  html, body {
    width: 1200px; height: 675px; overflow: hidden;
    background: var(--backdrop);
    font-family: "Open Sans", Arial, sans-serif;
  }
  .canvas {
    position: relative; width: 1200px; height: 675px;
    display: flex; align-items: center; justify-content: center; gap: 60px;
  }
  .card { box-shadow: 0 14px 30px rgba(0,0,0,.35); }

  /* Front */
  .card-front {
    width: 300px; height: 525px; background: var(--card-white);
    color: var(--ink-dark);
    display: flex; flex-direction: column; align-items: center;
    padding: 64px 24px 0; text-align: center;
  }
  .front-brand {
    font-weight: 800; font-size: 25px; line-height: 1.1;
    text-transform: uppercase; letter-spacing: .5px;
    width: 220px; color: var(--ink-dark);
  }
  .person { margin-top: 104px; }
  .person-name { font-weight: 600; font-size: 30px; line-height: 1; }
  .person-role { font-size: 14px; color: var(--ink-grey); margin-top: 2px; }
  .icon-rule {
    display: flex; align-items: center; gap: 6px; margin-top: 18px;
  }
  .icon-rule .rule { width: 62px; height: 1.5px; background: var(--rule-dark); }
  .icon-rule svg { width: 22px; height: 22px; }
  .contact { margin-top: 12px; font-size: 12.5px; font-weight: 600; line-height: 1.35; }
  .address { margin-top: 26px; font-size: 15px; line-height: 1.4; }

  /* Back */
  .card-back {
    width: 525px; height: 300px; background: var(--card-black);
    color: var(--ink-light);
    display: flex; flex-direction: column; align-items: center; justify-content: center;
    text-align: center;
  }
  .back-brand {
    font-weight: 800; font-size: 44px; line-height: 1.05;
    text-transform: uppercase; letter-spacing: 1px; color: var(--ink-light);
  }
  .social-rule { display: flex; align-items: center; gap: 8px; margin-top: 34px; }
  .social-rule .rule { width: 70px; height: 1px; background: var(--rule-light); }
  .social-dot { width: 14px; height: 14px; border: 1.5px solid var(--rule-light); border-radius: 50%; }
  .handle { margin-top: 8px; font-size: 12px; color: var(--rule-light); letter-spacing: .3px; }
</style>
</head>
<body>
<main class="canvas">
  <section class="card card-front" aria-label="Business card front">
    <div class="front-brand">Brisk Copper Atlas</div>
    <div class="person">
      <div class="person-name">Dorian</div>
      <div class="person-role">CEO</div>
    </div>
    <div class="icon-rule">
      <span class="rule"></span>
      <svg viewBox="0 0 22 22" aria-label="Email">
        <circle cx="11" cy="11" r="10" fill="none" stroke="#1a1a1a" stroke-width="1.3"/>
        <rect x="5.5" y="7.5" width="11" height="7" fill="none" stroke="#1a1a1a" stroke-width="1.1"/>
        <path d="M5.5 7.5 L11 12 L16.5 7.5" fill="none" stroke="#1a1a1a" stroke-width="1.1"/>
      </svg>
      <svg viewBox="0 0 22 22" aria-label="Website">
        <circle cx="11" cy="11" r="10" fill="none" stroke="#1a1a1a" stroke-width="1.3"/>
        <circle cx="11" cy="11" r="6" fill="none" stroke="#1a1a1a" stroke-width="1.1"/>
        <ellipse cx="11" cy="11" rx="2.6" ry="6" fill="none" stroke="#1a1a1a" stroke-width="1"/>
        <path d="M5 11 H17" stroke="#1a1a1a" stroke-width="1"/>
      </svg>
      <span class="rule"></span>
    </div>
    <div class="contact">
      <div>support@briskcopperatlas.com</div>
      <div>www.briskcopperatlas.com</div>
    </div>
    <div class="address">
      <div>72 Larkspur Lane,</div>
      <div>Fernhill, PA 19088</div>
    </div>
  </section>

  <section class="card card-back" aria-label="Business card back">
    <div class="back-brand">Brisk Copper<br>Atlas</div>
    <div class="social-rule">
      <span class="rule"></span>
      <span class="social-dot"></span>
      <span class="rule"></span>
    </div>
    <div class="handle">@briskcopperatlas</div>
  </section>
</main>
</body>
</html>
```